Marlin Freightways needs Bussiness cards!

Our new trucking company needs business cards!
We need the same design with two different names and emails, everything else it's the same.
I have included our original logo so we can use it for the design.
Note: the logo to be used is the o e with the buffalo on the right side, next to the letters B and E.

Target Market(s)

Trucking, refrigerated transportation, freight

Industry/Entity Type

Business

Contact Information for Business Card

Card #1:
Tomas Ruvalo
tomasruvalo@marlinfreightways.net
1-844-555-0193
(956)555-0172
3817 W. Alder Ave.
Pharr, TX 78590
www.marlinfreightways.net

Card#2:
Mirabel Quintana
mirabel@marlinfreightways.net
1-844-555-0193
(956)555-0172
3817 W. Alder Ave.
Pharr, TX 78590
www.marlinfreightways.net

Font styles to use
Sans Serif

Colors
0655a3
ec1f27
ffffff

Requirements
Must have
• our logo
Nice to have
• roads on background,

```html
<!DOCTYPE html>
<html lang="en">
<head>
<meta charset="utf-8">
<title>Marlin Freightways – Business Cards</title>
<link href="https://fonts.googleapis.com/css2?family=Poppins:wght@600;800&family=Open+Sans:wght@400;600&display=swap" rel="stylesheet">
<style>
  :root{
    --brand-blue:#0655a3;
    --brand-red:#ec1f27;
    --white:#ffffff;
    --card-paper:#f4f4f5;
    --card-black:#161616;
    --stage:#d9d6d0;
    --ink-muted:#c9cbd0;
  }
  *{box-sizing:border-box;margin:0;padding:0}
  html,body{width:1200px;height:780px;overflow:hidden}
  body{background:var(--stage);font-family:"Open Sans",Arial,sans-serif;position:relative}
  .card{position:absolute;top:236px;width:540px;height:309px;border-radius:4px;overflow:hidden;box-shadow:0 10px 28px rgba(0,0,0,.22)}

  /* front */
  .card-front{left:40px;background:var(--card-paper)}
  .front-watermark{position:absolute;right:40px;top:-20px;width:190px;height:170px;border-radius:50%;
    background:radial-gradient(circle at 45% 45%,rgba(150,155,165,.28),rgba(150,155,165,0) 70%)}
  .front-logo{position:absolute;left:26px;top:42px;display:flex;align-items:center;gap:10px}
  .logo-dot{width:22px;height:22px;border-radius:50%;background:var(--brand-red)}
  .logo-name{font-family:"Poppins",Arial,sans-serif;font-weight:800;font-size:30px;line-height:1;color:var(--brand-blue);letter-spacing:-.5px}
  .contact-band{position:absolute;left:0;height:56px;padding:7px 0 0 26px;color:var(--white)}
  .band-red{top:118px;width:330px;background:var(--brand-red)}
  .band-blue{top:174px;width:380px;background:var(--brand-blue)}
  .person-name{font-family:"Poppins",Arial,sans-serif;font-weight:600;font-size:20px;line-height:1.15}
  .person-email{display:flex;align-items:center;gap:6px;font-size:12.5px;line-height:1.4}
  .person-email svg{width:10px;height:8px;flex:none}
  .phones{position:absolute;left:26px;top:256px;display:flex;gap:38px}
  .phone{display:flex;align-items:center;gap:7px;font-size:15px;color:var(--brand-blue)}
  .phone-icon{width:17px;height:17px;border-radius:2px;background:var(--brand-red);display:flex;align-items:center;justify-content:center}
  .phone-icon svg{width:11px;height:11px}
  .website{position:absolute;right:22px;top:264px;font-size:12.5px;color:var(--brand-red)}

  /* back */
  .card-back{left:620px;background:var(--card-black)}
  .back-address{position:absolute;left:36px;bottom:34px;font-size:13px;color:var(--white);letter-spacing:.2px}
  .back-logo{position:absolute;right:40px;top:118px;display:flex;align-items:center;gap:12px}
  .back-logo .logo-dot{background:var(--white)}
  .back-logo .logo-name{color:var(--white);font-size:34px}
</style>
</head>
<body>

<section class="card card-front" aria-label="Business card front">
  <div class="front-watermark" role="img" aria-label="Faint brand emblem decoration"></div>

  <div class="front-logo">
    <span class="logo-dot"></span>
    <span class="logo-name">Marlin Freightways</span>
  </div>

  <div class="contact-band band-red">
    <p class="person-name">Tomas Ruvalo</p>
    <p class="person-email">
      <svg viewBox="0 0 10 8"><rect x=".5" y=".5" width="9" height="7" fill="none" stroke="#fff"/><path d="M.5 .5 5 4.5 9.5 .5" fill="none" stroke="#fff"/></svg>
      tomasruvalo@marlinfreightways.net
    </p>
  </div>

  <div class="contact-band band-blue">
    <p class="person-name">Mirabel Quintana</p>
    <p class="person-email">
      <svg viewBox="0 0 10 8"><rect x=".5" y=".5" width="9" height="7" fill="none" stroke="#fff"/><path d="M.5 .5 5 4.5 9.5 .5" fill="none" stroke="#fff"/></svg>
      mirabel@marlinfreightways.net
    </p>
  </div>

  <div class="phones">
    <p class="phone">
      <span class="phone-icon"><svg viewBox="0 0 24 24"><path fill="#fff" d="M6.6 10.8a15.1 15.1 0 0 0 6.6 6.6l2.2-2.2c.3-.3.7-.4 1-.2 1.1.4 2.3.6 3.6.6.6 0 1 .4 1 1V20c0 .6-.4 1-1 1A17 17 0 0 1 3 4c0-.6.4-1 1-1h3.5c.6 0 1 .4 1 1 0 1.3.2 2.5.6 3.6.1.3 0 .7-.2 1z"/></svg></span>
      1-844-555-0193
    </p>
    <p class="phone">
      <span class="phone-icon"><svg viewBox="0 0 24 24"><path fill="#fff" d="M6.6 10.8a15.1 15.1 0 0 0 6.6 6.6l2.2-2.2c.3-.3.7-.4 1-.2 1.1.4 2.3.6 3.6.6.6 0 1 .4 1 1V20c0 .6-.4 1-1 1A17 17 0 0 1 3 4c0-.6.4-1 1-1h3.5c.6 0 1 .4 1 1 0 1.3.2 2.5.6 3.6.1.3 0 .7-.2 1z"/></svg></span>
      (956)555-0172
    </p>
  </div>

  <p class="website">www.marlinfreightways.net</p>
</section>

<section class="card card-back" aria-label="Business card back">
  <div class="back-logo">
    <span class="logo-dot"></span>
    <span class="logo-name">Marlin Freightways</span>
  </div>
  <p class="back-address">3817 W. Alder Ave. Pharr, TX 78590</p>
</section>

</body>
</html>
```